Trifold for International Business Consulting firm

I have created a trifold piece (attached) that includes all the necessary information in a Word template; however, I need a professional that can make it look "current, international and modern". Our website, brightkeelpartners.com, should give an idea as to the style and color template we like.

```html
<!DOCTYPE html>
<html lang="en">
<head>
<meta charset="utf-8">
<title>Bright Keel Partners – Trifold</title>
<link href="https://fonts.googleapis.com/css2?family=Montserrat:wght@600;700;800&family=Open+Sans:wght@400;600&display=swap" rel="stylesheet">
<style>
  :root{
    --orange:#f26a21;
    --lime:#c6d84b;
    --lime-dark:#a9bd2e;
    --ink:#58595b;
    --muted:#8a8b8d;
    --paper:#f4f4f2;
    --panel-line:#dcdcd8;
    --stage:#e9e9e7;
  }
  *{box-sizing:border-box;margin:0;padding:0}
  html,body{width:1200px;height:3721px;overflow:hidden}
  body{background:var(--stage);font-family:"Open Sans",Arial,sans-serif;color:var(--ink);position:relative}

  .spread{position:absolute;left:60px;width:1080px;height:834px;background:var(--paper);display:flex;box-shadow:0 6px 24px rgba(0,0,0,.12)}
  .spread--outside{top:700px}
  .spread--inside{top:2140px}
  .band{position:absolute;left:0;width:100%;height:22px}
  .band--top{top:0}
  .band--bottom{bottom:0}

  .panel{width:360px;height:100%;padding:52px 30px 46px;position:relative;display:flex;flex-direction:column}
  .panel + .panel{border-left:1px solid var(--panel-line)}

  .section-head{background:var(--orange);color:#fff;font-family:"Montserrat",Arial,sans-serif;font-weight:700;font-size:15px;letter-spacing:.04em;text-transform:uppercase;padding:9px 12px;line-height:1.3;margin-bottom:14px}
  .body-copy{font-size:11.5px;line-height:1.6;margin-bottom:12px}
  .bullets{list-style:none;margin:0 0 14px}
  .bullets li{font-size:11.5px;line-height:1.55;padding-left:18px;position:relative;margin-bottom:7px}
  .bullets li::before{content:"";position:absolute;left:0;top:5px;width:8px;height:8px;background:var(--orange)}
  .callout{font-family:"Montserrat",Arial,sans-serif;font-weight:700;color:var(--orange);font-size:14px;line-height:1.45;text-align:center;margin-top:16px}

  .process-art{width:150px;height:150px;border-radius:50%;background:radial-gradient(circle at 40% 35%,#f7934f,var(--orange));margin:18px auto 0}

  .brand{display:flex;align-items:center;gap:10px;font-family:"Montserrat",Arial,sans-serif;font-weight:700;font-size:22px;color:var(--ink);letter-spacing:.06em;text-transform:uppercase}
  .brand-dot{width:14px;height:14px;border-radius:50%;background:var(--orange);flex:none}

  .address{font-size:11.5px;line-height:1.6;color:var(--muted);margin-top:18px}
  .address strong{color:var(--ink);font-weight:600}

  .cover-intro{font-family:"Montserrat",Arial,sans-serif;font-weight:600;font-size:12px;line-height:1.5;color:var(--muted);text-transform:uppercase;margin-top:70px}
  .cover-headline{font-family:"Montserrat",Arial,sans-serif;font-weight:800;font-size:24px;line-height:1.25;color:var(--orange);text-transform:uppercase;margin-top:26px}
  .cover-foot{font-size:11px;line-height:1.6;color:var(--muted);text-transform:uppercase;margin-top:auto}

  .back-panel{justify-content:flex-start}
  .back-panel .legal{margin-top:auto;font-size:10.5px;color:var(--muted)}
</style>
</head>
<body>

<!-- Outside of the trifold -->
<section class="spread spread--outside" aria-label="Trifold outside">
  <svg class="band band--top" viewBox="0 0 1080 22" preserveAspectRatio="none"><polygon points="0,0 1080,0 1080,8 0,16" fill="var(--lime)"/><polygon points="0,16 1080,8 1080,10 0,19" fill="var(--lime-dark)"/></svg>

  <article class="panel">
    <h2 class="section-head">Our three step process</h2>
    <p class="body-copy">Bright Keel Partners guides every client through a clear, proven path from first idea to a working presence abroad.</p>
    <ul class="bullets">
      <li>Assess: we study your market, rivals, costs and the legal setting to find the right fit.</li>
      <li>Plan: we build a practical entry strategy with budgets, timelines and local partners.</li>
      <li>Execute: we set up operations, hire teams and stay at your side as you grow.</li>
    </ul>
    <div class="process-art" role="img" aria-label="Illustration of a team working together inside an orange circle"></div>
    <p class="callout">Let us manage the entire process for you from strategy to execution and beyond.</p>
  </article>

  <article class="panel back-panel">
    <div class="brand"><span class="brand-dot"></span>Bright Keel Partners</div>
    <p class="address">
      <strong>Headquarters</strong><br>
      1420 Harbor Crest Ave, Suite 210<br>
      Tucson, AZ 85701<br>
      (520) 555-0148<br>
      hello@brightkeelpartners.com<br>
      brightkeelpartners.com
    </p>
    <p class="legal">© Bright Keel Partners, LLC</p>
  </article>

  <article class="panel">
    <div class="brand"><span class="brand-dot"></span>Bright Keel Partners</div>
    <p class="cover-intro">Our international business development process brings strategy and execution together</p>
    <h1 class="cover-headline">Our effective, innovative growth approach helps organizations accelerate and compete in a global world</h1>
    <p class="cover-foot">Business development<br>Market entry<br>Cultural management</p>
  </article>

  <svg class="band band--bottom" viewBox="0 0 1080 22" preserveAspectRatio="none"><polygon points="0,6 1080,14 1080,22 0,22" fill="var(--lime)"/><polygon points="0,3 1080,12 1080,14 0,6" fill="var(--lime-dark)"/></svg>
</section>

<!-- Inside of the trifold -->
<section class="spread spread--inside" aria-label="Trifold inside">
  <svg class="band band--top" viewBox="0 0 1080 22" preserveAspectRatio="none"><polygon points="0,0 1080,0 1080,8 0,16" fill="var(--lime)"/><polygon points="0,16 1080,8 1080,10 0,19" fill="var(--lime-dark)"/></svg>

  <article class="panel">
    <h2 class="section-head">Should we expand?</h2>
    <p class="body-copy">A decision to grow abroad is one of the most important choices a company makes. Bright Keel Partners helps leaders weigh risk and reward with clear data and honest advice before any money is spent.</p>
    <ul class="bullets">
      <li>How do your products compare with local offers in the new market?</li>
      <li>Is there real demand, and how large could your share become?</li>
      <li>What will it cost to enter, and when will you see a return?</li>
      <li>Which rules, taxes and permits apply to your industry?</li>
    </ul>
    <p class="body-copy">If you are ready to grow, contact us today to set up your first review.</p>
    <h2 class="section-head">How do we expand?</h2>
    <p class="body-copy">Once the case is made, we choose the best entry model for you, from export and distribution to joint ventures and new offices.</p>
  </article>

  <article class="panel">
    <h2 class="section-head">Which expansion opportunity is best for my company?</h2>
    <p class="body-copy">Each opportunity has its own pros and cons for growth, which can be deeply dependent on the country of expansion and your budget. Some markets are friendlier for new business, while others reward patience and strong local ties.</p>
    <p class="body-copy">To determine the best way forward, it is good practice to seek counsel from several sources. Our network spans many fields and lets us compare options side by side for you.</p>
    <h2 class="section-head">Working with specialists</h2>
    <p class="body-copy">We have spent years developing relationships with accounting, legal and financial specialists needed for international growth. We have trusted advisors in each market we serve, ready to support your team.</p>
    <p class="body-copy">Instead of searching through groups of consultants on your own, you work with one partner who brings the right people together at the right time.</p>
  </article>

  <article class="panel">
    <h2 class="section-head">Cultural management</h2>
    <p class="body-copy">In addition to international business consulting services, we have expertise in the cultural side of doing business across borders and between teams.</p>
    <p class="body-copy">With more than 20 years of experience in training and coaching, we help managers and staff work well together, avoid costly misunderstandings and build lasting trust with clients and partners.</p>
    <p class="body-copy">Our programs cover communication, negotiation and leadership, and can be tailored to your company and region.</p>
    <p class="address">
      <strong>Headquarters</strong><br>
      Bright Keel Partners<br>
      1420 Harbor Crest Ave, Suite 210<br>
      Tucson, AZ 85701<br>
      (520) 555-0148<br>
      hello@brightkeelpartners.com<br>
      brightkeelpartners.com
    </p>
    <p class="legal address">© Bright Keel Partners, LLC</p>
  </article>

  <svg class="band band--bottom" viewBox="0 0 1080 22" preserveAspectRatio="none"><polygon points="0,6 1080,14 1080,22 0,22" fill="var(--lime)"/><polygon points="0,3 1080,12 1080,14 0,6" fill="var(--lime-dark)"/></svg>
</section>

</body>
</html>
```